I need someone to design a flyer for my business website. I would like a designer to use my website information to create a flyer. You can view a preliminary example of the website at www.bluvan-tours.example, although the real website will go live in a few days at www.bluvan-tours.example.

*** Summarize the information on the website. DO NOT cut and past. The students will typically be on their way to class when they will see this flyer. This flyer must not only grab their attention, but also give the relevant information as concisely as possible.

*** Be sure to include the following: Name of company in bold on the flyer, website address (www.bluvan-tours.example), and the service we provide (coach transportation).
Updates

Project Deadline Extended
Reason: The Thanksgiving holiday made it difficult for many designers to submit their designs. Therefore, Bluvan Tours will be extending our deadline by 2 days. Please make sure to have your final designs in by this 3:24pm on November 29th.

Project Deadline Extended
Reason: Updated note in the brief: *** Please develop a unique summary for the information on the website (www.bluvan-tours.example). Do not copy and past the information. This will be the last extention! I am impressed with all of your submissions. Feel free to play around more with your advertisement to make it stand out to students. They are typically going to be on their way to class when they see this flyer, so they need the important information and only the important information! Best wishes, Bluvan Tours

I have attached a picture of the actual website that will appear at www.bluvan-tours.example. Try to make the flyer represent the website.

Great submissions so far from all of you! I'm quite impressed!

Target Market(s)

College Students! They will be rushing to their classes when they see this flyer.

Industry/Entity Type

Business

Requirements
Must have
• *** Be sure to include the following: Name of company in bold on the flyer, website address (www.bluvan-tours.example), and the service we provide (coach transportation).
Nice to have
• I have attached a picture of the actual website that will appear at www.bluvan-tours.example. Try to make the flyer represent the website.
Should not have
• *** Summarize the information on the website. DO NOT cut and past. The students will typically be on their way to class when they will see this flyer. This flyer must not only grab their attention, but also give the relevant information as concisely as possible.

```html
<!DOCTYPE html>
<html lang="en">
<head>
<meta charset="utf-8">
<title>Bluvan Tours – Ski &amp; Snowboard Coach Transportation</title>
<link rel="stylesheet" href="https://fonts.googleapis.com/css2?family=Rubik+Dirt&family=Oswald:wght@500;600;700&family=Open+Sans:wght@400;700&family=Archivo+Narrow:ital,wght@0,700;1,700&display=swap">
<style>
  :root{
    --sky-top:#2f86cf;
    --sky-mid:#7fc0ea;
    --sky-low:#cfe9f8;
    --snow:#e9f5fc;
    --snow-deep:#b9dbef;
    --navy:#1c2f5a;
    --ink:#1d3466;
    --yellow:#f7d417;
    --white:#ffffff;
    --photo-red:#c8342a;
    --photo-khaki:#cdbf9f;
    --photo-teal:#5fb3cf;
  }
  *{margin:0;padding:0;box-sizing:border-box}
  html,body{width:873px;height:1200px;overflow:hidden;background:var(--snow)}
  .flyer{position:relative;width:873px;height:1200px;overflow:hidden}

  .scenery{position:absolute;inset:0;
    background:linear-gradient(180deg,var(--sky-top) 0%,var(--sky-mid) 22%,var(--sky-low) 38%,var(--snow) 46%,var(--white) 62%,var(--snow-deep) 80%,var(--snow) 100%)}

  .photo{position:absolute}
  .photo--skier{left:50px;top:120px;width:270px;height:520px;border-radius:40% 40% 30% 30%/20% 20% 15% 15%;
    background:linear-gradient(180deg,rgba(200,52,42,0) 0%,var(--photo-red) 14%,var(--photo-red) 45%,var(--photo-khaki) 62%,rgba(205,191,159,.4) 90%,rgba(205,191,159,0) 100%);opacity:.85}
  .photo--boarder{left:700px;top:752px;width:140px;height:145px;border-radius:45%;
    background:radial-gradient(circle,var(--photo-red) 0%,rgba(200,52,42,.5) 45%,rgba(200,52,42,0) 72%)}
  .photo--rider{left:635px;top:985px;width:238px;height:215px;border-radius:50% 50% 0 0;
    background:radial-gradient(ellipse at 50% 45%,#f0c9a8 0%,var(--photo-teal) 55%,rgba(95,179,207,.2) 100%)}

  .brand-title{position:absolute;z-index:2;left:0;top:24px;width:873px;text-align:center;white-space:nowrap;
    font-family:"Rubik Dirt",sans-serif;font-weight:400;font-size:86px;line-height:1;color:var(--white);
    letter-spacing:3px;text-shadow:0 2px 6px rgba(20,60,110,.35)}

  .headline{position:absolute;z-index:2;left:350px;top:190px;width:490px;text-align:center;white-space:nowrap;
    font-family:"Oswald",sans-serif;font-weight:700;font-size:52px;line-height:54px;
    color:var(--yellow);transform:rotate(-5deg);text-shadow:2px 2px 4px rgba(0,0,0,.35);text-transform:uppercase}
  .headline .light{color:var(--white)}

  .banner{position:absolute;z-index:2;left:232px;top:445px;width:660px;height:180px;transform:rotate(4deg)}
  .banner svg{position:absolute;inset:0}
  .banner__text{position:absolute;left:40px;top:36px;width:590px;text-align:center;
    font-family:"Oswald",sans-serif;font-weight:600;font-size:20px;line-height:29px;color:var(--yellow)}
  .banner__text strong{color:var(--white);font-weight:700}

  .details{position:absolute;z-index:2;left:158px;top:630px;width:580px;transform:rotate(4deg);transform-origin:left top;
    font-family:"Open Sans",sans-serif;color:var(--ink);font-size:14.5px;line-height:18px}
  .details h2{font-size:16px;font-weight:700;margin-bottom:2px;color:var(--navy)}
  .details p{margin-bottom:24px}
  .details .wrap-short{width:515px}

  .contact{position:absolute;z-index:2;left:40px;top:1130px}
  .contact__label{font-family:"Archivo Narrow",sans-serif;font-style:italic;font-weight:700;font-size:19px;color:var(--navy)}
  .contact__url{font-family:"Oswald",sans-serif;font-weight:700;font-size:38px;line-height:42px;color:var(--navy);letter-spacing:.3px}
</style>
</head>
<body>
<main class="flyer">
  <div class="scenery" role="img" aria-label="Snowy mountain landscape under a bright blue winter sky"></div>

  <div class="photo photo--skier" role="img" aria-label="Photo of a freestyle skier in a red hoodie jumping with skis crossed"></div>

  <h1 class="brand-title">BLUVAN TOURS</h1>

  <p class="headline">Love skiing?<br>Love snowboarding?<br>Then <span class="light">Bluvan Tours</span><br>is <span class="light">for you!</span></p>

  <div class="banner">
    <svg viewBox="0 0 660 180" width="660" height="180" aria-hidden="true">
      <path fill="#1c2f5a" d="M24 22 L70 14 L120 20 L180 10 L260 18 L330 8 L420 16 L500 6 L580 14 L640 8 L652 40 L646 90 L654 140 L620 150 L600 176 L585 150 L540 156 L520 172 L505 152 L450 150 L430 168 L415 148 L360 146 L340 162 L325 144 L260 140 L240 160 L226 140 L160 138 L140 156 L128 136 L60 132 L40 150 L34 128 L8 120 L16 80 L4 46 Z"/>
    </svg>
    <p class="banner__text">NSU student in need of a break from a hectic week? Ride with us for reliable, low-cost <strong>COACH TRANSPORTATION</strong> to the best ski parks around Lakeport, Northland!</p>
  </div>

  <div class="photo photo--boarder" role="img" aria-label="Photo of a snowboarder in a red jacket mid-air"></div>

  <div class="details">
    <section>
      <h2>Who We Are</h2>
      <p>A student-run company from NSU, Bluvan Tours takes you safely to Ridgeback Peak and Fernhollow Mountain and back again, all winter long.</p>
    </section>
    <section>
      <h2>What We Offer</h2>
      <p class="wrap-short">Comfortable coach buses run on set dates each month, with departure and return times listed on our Bus Itinerary page. Check the 2011-2012 calendar online to plan your next trip to the slopes.</p>
      <p class="wrap-short">Every ride is part of the fun! A Bluvan crew member hosts each bus, with prize giveaways, free magazines, the odd pizza party and other extras on board.</p>
    </section>
    <section>
      <h2>Your specific needs</h2>
      <p class="wrap-short">Tell us what works for you on our blog. Share your thoughts on dates, times and prices, or pitch a brand-new idea. We read every comment and answer your requests, so jump in and post!</p>
    </section>
  </div>

  <div class="photo photo--rider" role="img" aria-label="Photo of a smiling snowboarder in goggles and a knit hat"></div>

  <footer class="contact">
    <p class="contact__label">Find more at:</p>
    <p class="contact__url">www.bluvan-tours.example</p>
  </footer>
</main>
</body>
</html>
```